Letterhead for New Orthopaedic Surgery Practice

My husband and I are starting our own practice named RB Spine & Vitality Center. We would like to create a nice simple but high class letterhead that doesn't use too much solid color ink when printing. I like the colors dark blue, gold, yellow. Open to other suggestions. We will need to list him and I both on the top of the letterhead. Here is the important information:
Lucinda Perrow, M.D. - Hand and Upper Extremity Surgery
Abena Quist, M.D. - Hip & Knee Replacement/General Orthopaedic Surgery
Location: 18735 North Harlow Pkwy
Coral Springs, FL 33071
Phone: 954-218-4650
Fax: 954-582-1346
Email: info@myrbspine.com

The only thing is that the phone and fax numbers will change once we get into our space. I just want to get the design started. I am including several documents which are my previous practice letterhead, my current procedure room letterhead, and our new Logo. The other letterheads are just for examples but please think outside of the box! We would love to see some great designs.

Colors
0054AA
0677BA
7BADD7
CADEEF
E8F1F8
0094D4
00A9DD
6FCCEA
C7EBF8
E9F6FB

Requirements
Must have
• class, elegance, luxury

```html
<!DOCTYPE html>
<html lang="en">
<head>
<meta charset="utf-8">
<title>RB Spine &amp; Vitality Center — Letterhead</title>
<link rel="stylesheet" href="https://fonts.googleapis.com/css2?family=Libre+Baskerville:wght@400;700&display=swap">
<style>
  :root {
    --backdrop: #a2a2a2;
    --paper: #ffffff;
    --navy: #1d2b57;
    --gold: #c9a052;
  }
  * { box-sizing: border-box; margin: 0; padding: 0; }
  html, body {
    width: 1200px;
    height: 968px;
    overflow: hidden;
    background: var(--backdrop);
  }
  .letterhead {
    position: absolute;
    left: 289px;
    top: 44px;
    width: 622px;
    height: 880px;
    background: var(--paper);
    font-family: "Libre Baskerville", Georgia, serif;
    color: var(--navy);
  }
  .brand {
    position: absolute;
    left: 38px;
    top: 52px;
    display: flex;
    align-items: center;
    gap: 12px;
  }
  .brand-circle {
    width: 46px;
    height: 46px;
    border: 1.5px solid var(--gold);
    border-radius: 50%;
    flex: none;
  }
  .brand-name {
    font-size: 11px;
    font-weight: 400;
    letter-spacing: 0.14em;
    text-transform: uppercase;
    line-height: 1.55;
    color: var(--navy);
  }
  .physicians {
    position: absolute;
    left: 342px;
    top: 44px;
    width: 250px;
  }
  .physician-name {
    font-size: 10.5px;
    font-weight: 700;
    color: var(--navy);
    line-height: 1.3;
  }
  .physician-specialty {
    font-size: 9px;
    font-weight: 400;
    color: var(--gold);
    line-height: 1.4;
  }
  .physician-divider {
    width: 176px;
    height: 1px;
    background: var(--gold);
    margin: 15px 0 18px;
  }
  .footer-band {
    position: absolute;
    left: 0;
    right: 0;
    top: 824px;
    height: 6px;
    background: var(--navy);
  }
  .footer-rule {
    position: absolute;
    left: 0;
    right: 0;
    top: 833px;
    height: 1px;
    background: var(--gold);
  }
  .contact-line {
    position: absolute;
    left: 36px;
    right: 36px;
    top: 852px;
    display: flex;
    justify-content: space-between;
    align-items: center;
    list-style: none;
  }
  .contact-item {
    display: flex;
    align-items: center;
    gap: 6px;
    font-size: 8px;
    font-weight: 700;
    color: var(--navy);
    white-space: nowrap;
  }
  .contact-icon {
    width: 9px;
    height: 9px;
    flex: none;
  }
</style>
</head>
<body>
  <main class="letterhead">
    <header>
      <div class="brand">
        <span class="brand-circle"></span>
        <span class="brand-name">RB Spine &amp;<br>Vitality Center</span>
      </div>

      <section class="physicians">
        <p class="physician-name">Lucinda Perrow, M.D.</p>
        <p class="physician-specialty">Hand and Upper Extremity Surgery</p>
        <div class="physician-divider"></div>
        <p class="physician-name">Abena Quist, M.D.</p>
        <p class="physician-specialty">Hip &amp; Knee Replacement/General Orthopaedic Surgery</p>
      </section>
    </header>

    <footer>
      <div class="footer-band"></div>
      <div class="footer-rule"></div>
      <ul class="contact-line">
        <li class="contact-item">
          <svg class="contact-icon" viewBox="0 0 10 10" aria-hidden="true">
            <path d="M5 0.5a3.2 3.2 0 0 0-3.2 3.2C1.8 6 5 9.5 5 9.5S8.2 6 8.2 3.7A3.2 3.2 0 0 0 5 0.5z" fill="var(--gold)"/>
            <circle cx="5" cy="3.7" r="1.2" fill="#fff"/>
          </svg>
          18735 North Harlow Pkwy Coral Springs, FL 33071
        </li>
        <li class="contact-item">
          <svg class="contact-icon" viewBox="0 0 10 10" aria-hidden="true">
            <path d="M2.2 0.8l1.6 1.8-0.9 1.3c0.6 1.3 1.6 2.3 2.9 2.9l1.3-0.9 1.8 1.6-1 1.6C4.6 9 1 5.4 0.8 1.8z" fill="var(--gold)"/>
          </svg>
          954-218-4650
        </li>
        <li class="contact-item">
          <svg class="contact-icon" viewBox="0 0 10 10" aria-hidden="true">
            <rect x="2.5" y="0.8" width="5" height="3" fill="none" stroke="var(--gold)" stroke-width="1"/>
            <rect x="0.8" y="3.8" width="8.4" height="3.8" rx="0.6" fill="var(--gold)"/>
            <rect x="2.5" y="6.5" width="5" height="2.7" fill="#fff" stroke="var(--gold)" stroke-width="1"/>
          </svg>
          954-582-1346
        </li>
        <li class="contact-item">
          <svg class="contact-icon" viewBox="0 0 10 10" aria-hidden="true">
            <rect x="0.8" y="2" width="8.4" height="6" fill="none" stroke="var(--gold)" stroke-width="1"/>
            <path d="M0.8 2L5 5.6 9.2 2" fill="none" stroke="var(--gold)" stroke-width="1"/>
          </svg>
          info@myrbspine.com
        </li>
      </ul>
    </footer>
  </main>
</body>
</html>
```